Indigenous Mentoring Masterclass

We are a small Indigenous owned company that specializes in mentoring training for anybody who mentors Indigenous mentees: www.taranlink.com.au

We would like a brochure advertising an upcoming training course being held Parramatta, Sydney, NSW. The brochure should show the course goals and objectives (course syllabus attached)

The brochure to have colouring similar to loggo attached.

The final design should advertise a sharp two day course delivered by specialist Indigenous trainers.
Updates

Hi Everyone,

Hi Res Loggo updated for your use.  Please let me know if you require further help.

Regards

Target Market(s)

Anybody working in the Indigenous Australian domain.

Industry/Entity Type

Advertising

Requirements
Must have
• This new and improved skills - based course has been sharpened to a 2 day program to focus mentors on deep mentoring and therefore creating transformational changes with mentees.

Brochure will have a focus on the trainer capability.

Our Trainers
Under the leadership of TLK’s remarkably accomplished Directors Marcella Dunphy and Gordon Pelkey, the company has gained a reputation across a range of organisations and sectors as a dependable supplier of superior cutting-edge training, facilitation and consultative services, consistently providing the greatest value for money.
The TLK team is made up of highly qualified and practiced individuals with a passion and commitment to providing fresh, innovative and proven approaches to effective training delivery and group facilitation. We are self-motivated and results-focused individuals who achieve proven results for our clients. TLK’s Directors bring together highly competent project teams to achieve proven specific client objectives. These teams can comprise of a number of expert associates in relevant specialist fields, and are linked in to help do so. You will have an opportunity to spend two days with these Directors and ask how you can leverage your mentoring skills within your organization.
TLKs Business lines: agile and scrum, tribal leadership, global diversity and sustainability, culture hacking, leadership, community and organization development, change, coaching and mentoring.

Learning Objectives
After completing the course, you will learn powerful new distinctions that will improve your knowledge and practice base to leverage your mentoring conversations.
Learn practical problem solving and solution focused methods to address mentee concerns and understand and manage moods with yourself, mentees and others.

Learning Goals

To appreciate the power of language and conversations in getting work done, discuss with other like-minded participants the uncertainty of change and how it impacts Indigenous Australians.

Please note: picture of Marcella and Gordon attached as the couple.
Nice to have
• Loggo
Your ideas and creativity based on the course syllabus
An editable document so that I can insert and or change venue details whenever I deliver training in another state.

REGISTRATION DETAILS

enquiries to Marcella Dunphy 1800 394 517

COMPANY DETAILS

www.taranlink.com.au
PO Box 836, Wyong, NSW 2259

```html
<!DOCTYPE html>
<html lang="en">
<head>
<meta charset="utf-8">
<title>Deep Mentoring for Mentors – Course Syllabus</title>
<link href="https://fonts.googleapis.com/css2?family=Roboto+Condensed:wght@400;700&family=Source+Sans+3:wght@400;600&display=swap" rel="stylesheet">
<style>
  :root{
    --page-bg:#d6d6d6;
    --paper-light:#ececec;
    --band-grey:#6b6b6b;
    --bar-grey:#a8a8a8;
    --ink-dark:#231f20;
    --ink-text:#1e1e1e;
    --title-grey:#b8b8b8;
    --white:#ffffff;
    --accent-red:#b0283a;
    --accent-orange:#e8a021;
    --photo-tone:#7f8f6e;
    --sketch-tone:#f6f1f1;
    --faint-mark:#e6c9cc;
  }
  *{box-sizing:border-box;margin:0;padding:0}
  html,body{width:1200px;height:960px;overflow:hidden;background:var(--page-bg)}
  h1,h2{font-weight:400}
  .spread{position:absolute;left:8px;top:62px;width:1184px;height:836px;box-shadow:0 4px 14px rgba(0,0,0,.25)}
  .panel{position:absolute;top:0;height:836px;overflow:hidden}
  .panel--back{left:0;width:592px;background:var(--paper-light);color:var(--ink-text)}
  .panel--front{left:592px;width:592px;background:var(--ink-dark);color:var(--white)}
  .abs{position:absolute}

  .contact-band{left:0;top:82px;width:592px;height:124px;background:var(--band-grey)}
  .directors-photo{left:34px;top:0;width:247px;height:338px;background:linear-gradient(180deg,#5f7a4c 0%,var(--photo-tone) 55%,#9a9a98 100%)}
  .contact{left:298px;top:100px;font-family:"Roboto Condensed",sans-serif;font-size:22px;line-height:25px;color:var(--white);font-style:normal}
  .faint-mark{left:305px;top:215px}
  .goals-title{left:49px;top:424px;font-family:"Roboto Condensed",sans-serif;font-size:25px;color:var(--ink-text);white-space:nowrap}
  .goals{left:49px;top:462px;width:500px;list-style:none;font-family:"Source Sans 3",sans-serif;font-size:14.5px;line-height:16px}
  .goals li{position:relative;padding-left:13px;margin-bottom:7px}
  .goals li::before{content:"•";position:absolute;left:0;top:0}
  .footer-band{left:0;top:773px;width:592px;height:63px;background:var(--band-grey)}

  .brand-box{left:0;top:82px;width:209px;height:124px;background:var(--paper-light);display:flex;align-items:center;padding-left:28px;gap:10px}
  .brand-name{font-family:"Roboto Condensed",sans-serif;font-weight:700;font-size:54px;color:var(--ink-dark);line-height:1}
  .brand-dot{width:40px;height:40px;border-radius:50%;background:var(--accent-red)}
  .sketch{left:199px;top:0;width:393px;height:271px;background:linear-gradient(135deg,var(--white) 0%,var(--sketch-tone) 70%,#e3e0df 100%)}
  .course-title{left:21px;top:296px;font-family:"Roboto Condensed",sans-serif;font-size:41px;line-height:46px;color:var(--title-grey);white-space:nowrap}
  .syllabus-bar{left:0;top:359px;width:591px;height:34px;background:var(--bar-grey);font-family:"Roboto Condensed",sans-serif;font-size:25px;line-height:34px;padding-left:44px;color:var(--white);white-space:nowrap}
  .about-marker{left:0;top:426px;width:40px;height:29px;background:var(--accent-red)}
  .about-lead{left:46px;top:421px;font-family:"Roboto Condensed",sans-serif;font-size:25px;line-height:34px;color:var(--accent-orange);white-space:nowrap}
  .about-bar{left:161px;top:421px;width:430px;height:34px;background:var(--bar-grey);font-family:"Roboto Condensed",sans-serif;font-size:25px;line-height:34px;padding-left:4px;color:var(--ink-dark)}
  .section-title{font-family:"Roboto Condensed",sans-serif;font-size:25px;line-height:30px;color:#d8d8d8;white-space:nowrap}
  .mission-title{left:45px;top:482px}
  .mission-text{left:45px;top:513px;width:530px;font-family:"Source Sans 3",sans-serif;font-size:14.5px;line-height:16px}
  .objectives-title{left:49px;top:566px}
  .objectives-lead{left:49px;top:606px;width:500px;font-family:"Source Sans 3",sans-serif;font-size:14.5px;line-height:18px;color:var(--accent-orange)}
  .objectives{left:49px;top:655px;width:520px;list-style:none;font-family:"Source Sans 3",sans-serif;font-size:11.5px;line-height:14px}
  .objectives li{position:relative;padding-left:10px;margin-bottom:8px}
  .objectives li::before{content:">";position:absolute;left:0;top:0}
</style>
</head>
<body>
<main class="spread">
  <section class="panel panel--back" aria-label="Back cover">
    <div class="abs contact-band"></div>
    <div class="abs directors-photo" role="img" aria-label="Photograph of the two directors standing together on a leafy street"></div>
    <address class="abs contact">
      Call us: 61 2 4907 3258<br>
      Email: hello@taranlink.com.au<br>
      www.taranlink.com.au
    </address>
    <svg class="abs faint-mark" width="220" height="220" viewBox="0 0 220 220" role="img" aria-label="Faint brand circle">
      <circle cx="110" cy="110" r="95" fill="var(--faint-mark)"/>
    </svg>
    <h2 class="abs goals-title">Learning Goals</h2>
    <ul class="abs goals">
      <li>To appreciate the power of language and conversation in getting work done, the quality of workplace relationships, and job satisfaction in 21st Century workplaces;</li>
      <li>Discuss the importance of living in a context that you create for your mentee;</li>
      <li>Discuss with other like-minded participants the uncertainty of continual and massive upheaval and change and how that impacts Indigenous Australians and the implications for existence</li>
      <li>Understand the key conversation and language distinctions and how to use them to good effect;</li>
      <li>How to manage your own, and the moods of others to avoid the often unintended destructive and negative impact of certain moods in work teams and workplaces;</li>
      <li>Appreciate how critically important integrity and trust are to positive working relationships and getting work done, and practical ways as to how you can contribute to that.</li>
    </ul>
    <div class="abs footer-band"></div>
  </section>

  <section class="panel panel--front" aria-label="Front cover">
    <div class="abs brand-box">
      <span class="brand-name">TLK</span>
      <span class="brand-dot" aria-hidden="true"></span>
    </div>
    <div class="abs sketch" role="img" aria-label="Hand drawn whiteboard diagram linking success with vision, teamwork, lead by example, inspire, goals, mentor, teach and motivate"></div>
    <h1 class="abs course-title">DEEP MENTORING FOR MENTORS</h1>
    <div class="abs syllabus-bar">COURSE&nbsp; SYLLABUS</div>
    <div class="abs about-marker"></div>
    <div class="abs about-lead">ABOUT THE</div>
    <div class="abs about-bar">COURSE</div>
    <h2 class="abs section-title mission-title">Course Mission</h2>
    <p class="abs mission-text">That as a mentor you will understand the principals of deep mentoring and how to create powerful, constructive conversationsto get what you want.</p>
    <h2 class="abs section-title objectives-title">Learning Objectives</h2>
    <p class="abs objectives-lead">After completing the course, you will learn powerful new distinctions that will improve your knowledge and practice base to:</p>
    <ul class="abs objectives">
      <li>acquire powerful distinctions in conversation and language that give you access to unlock the benefits of mentoring;</li>
      <li>develop conversation and language skills that will increase your capacity to getting your voice heard, influencing your mentee and improving the quality of your immediate working relationships</li>
      <li>learn practical problem solving and solution focused methods to address&nbsp; workplace concerns with your mentee;</li>
      <li>Improve personal work effectiveness and your own productivity and</li>
      <li>Understand and manage moods in the workplace-your own and others.</li>
    </ul>
  </section>
</main>
</body>
</html>
```